Clean, Fresh Business Card Design Needed

We need a business card design for a new business we have taken over called "Bonders and Fillers". We got a logo through this website which i have attached. We are wanting something that is vibrant but clean and fresh. Our business mainly sells glue. Maybe a cool design/slogan on the back? Modern, sleek.

Industry/Entity Type

Business

Contact Information for Business Card

Name: Ewan Tressider, Managing Director. Address: 164 Kelmond Road, Tauranga 3117, Phone: 07 462 3947 Mobile: 021 354 921 Fax: 07 462 5086 Email: bondfill.mail@pelorix.co.nz, Web: www.stickwarex.co.nz

Font styles to use
Serif

Requirements
Must have
• All business card details, logo.
Nice to have
• Design, slogan on back of card

```html
<!DOCTYPE html>
<html lang="en">
<head>
<meta charset="utf-8">
<title>Bonders and Fillers – Business Card</title>
<link rel="stylesheet" href="https://fonts.googleapis.com/css2?family=Marcellus&family=Open+Sans:wght@400;700&display=swap">
<style>
  :root {
    --stage: #d9d9d9;
    --charcoal: #333333;
    --paper: #ffffff;
    --paper-shade: #ececec;
    --signal-yellow: #f4e81a;
    --brand-navy: #24307a;
    --ink: #111111;
    --muted: #e4e4e4;
  }
  * { box-sizing: border-box; margin: 0; padding: 0; }
  html, body {
    width: 1200px; height: 900px; overflow: hidden;
    background: var(--stage);
  }
  .canvas { position: relative; width: 1200px; height: 900px; }

  .card {
    position: absolute;
    width: 660px; height: 378px;
    overflow: hidden;
    box-shadow: 0 6px 18px rgba(0,0,0,.25);
    background: var(--charcoal);
  }

  /* ---------- front ---------- */
  .card--front { left: 70px; top: 60px; }
  .front__header {
    position: absolute; left: 0; top: 0; width: 100%; height: 100px;
    background: linear-gradient(180deg, var(--paper) 0%, var(--paper-shade) 100%);
  }
  .front__body { position: absolute; left: 0; top: 100px; width: 100%; height: 148px; background: var(--charcoal); }
  .front__rule { position: absolute; left: 0; top: 248px; width: 100%; height: 12px; background: var(--paper); }
  .front__band { position: absolute; left: 0; top: 260px; width: 100%; height: 86px; background: var(--signal-yellow); }
  .front__footer { position: absolute; left: 0; top: 346px; width: 100%; height: 32px; background: var(--paper); }

  .brand {
    display: flex; align-items: center; gap: 10px;
    font-family: "Marcellus", serif;
    color: var(--ink);
    text-transform: uppercase;
    white-space: nowrap;
  }
  .brand__mark { display: block; background: var(--brand-navy); border-radius: 3px; flex: none; }
  .front__header .brand { position: absolute; right: 34px; top: 24px; font-size: 26px; letter-spacing: 1px; }
  .front__header .brand__mark { width: 50px; height: 50px; }

  .contact-list {
    position: absolute; left: 62px; top: 124px;
    list-style: none;
    font-family: "Open Sans", sans-serif;
    font-size: 15px; color: var(--paper);
  }
  .contact-list li { display: flex; align-items: center; height: 20px; }
  .contact-list svg { width: 14px; height: 14px; margin-right: 36px; flex: none; }

  .person {
    position: absolute; right: 60px; top: 128px; text-align: center;
    font-family: "Open Sans", sans-serif; color: var(--paper);
  }
  .person__name { font-size: 21px; font-weight: 400; }
  .person__surname { color: var(--signal-yellow); font-weight: 700; }
  .person__role { font-size: 14px; margin-top: 2px; }

  /* ---------- back ---------- */
  .card--back { left: 470px; top: 470px; }
  .back__rule-top { position: absolute; left: 0; top: 56px; width: 100%; height: 12px; background: var(--paper); }
  .back__band {
    position: absolute; left: 0; top: 68px; width: 100%; height: 104px;
    background: var(--signal-yellow);
    display: flex; align-items: center; justify-content: center;
  }
  .back__rule-bottom { position: absolute; left: 0; top: 172px; width: 100%; height: 12px; background: var(--paper); }
  .back__band .brand { font-size: 34px; letter-spacing: 2px; gap: 14px; }
  .back__band .brand__mark { width: 64px; height: 64px; }
</style>
</head>
<body>
<main class="canvas">

  <section class="card card--front" aria-label="Business card front">
    <div class="front__header">
      <div class="brand">
        <span class="brand__mark"></span>
        <span class="brand__name">Bonders and Fillers</span>
      </div>
    </div>
    <div class="front__body"></div>
    <div class="front__rule"></div>
    <div class="front__band"></div>
    <div class="front__footer"></div>

    <ul class="contact-list">
      <li>
        <svg viewBox="0 0 14 14" fill="none" stroke="#fff" stroke-width="1.4"><rect x="3.5" y="1" width="7" height="12" rx="1"/><line x1="6" y1="11" x2="8" y2="11"/></svg>
        021 354 921
      </li>
      <li>
        <svg viewBox="0 0 14 14" fill="#fff"><path d="M1 5c0-2 3-3 6-3s6 1 6 3v1h-3V5H4v1H1z"/><rect x="3" y="7" width="8" height="5" rx="1"/></svg>
        07 462 3947
      </li>
      <li>
        <svg viewBox="0 0 14 14" fill="#fff"><rect x="4" y="1" width="6" height="4"/><rect x="1" y="5" width="12" height="6" rx="1"/><rect x="4" y="9" width="6" height="4" fill="#333" stroke="#fff"/></svg>
        07 462 5086
      </li>
      <li>
        <svg viewBox="0 0 14 14" fill="none" stroke="#fff" stroke-width="1.4"><rect x="1" y="3" width="12" height="8"/><polyline points="1,3 7,8 13,3"/></svg>
        bondfill.mail@pelorix.co.nz
      </li>
      <li>
        <svg viewBox="0 0 14 14" fill="none" stroke="#fff" stroke-width="1.4"><rect x="1" y="2" width="12" height="8"/><line x1="4" y1="13" x2="10" y2="13"/><line x1="7" y1="10" x2="7" y2="13"/></svg>
        www.stickwarex.co.nz
      </li>
      <li>
        <svg viewBox="0 0 14 14" fill="#fff"><polygon points="7,1 13,7 11,7 11,13 8,13 8,9 6,9 6,13 3,13 3,7 1,7"/></svg>
        164 Kelmond Road, Tauranga 3117
      </li>
    </ul>

    <div class="person">
      <p class="person__name">Ewan <span class="person__surname">Tressider</span></p>
      <p class="person__role">Manager</p>
    </div>
  </section>

  <section class="card card--back" aria-label="Business card back">
    <div class="back__rule-top"></div>
    <div class="back__band">
      <div class="brand">
        <span class="brand__mark"></span>
        <span class="brand__name">Bonders and Fillers</span>
      </div>
    </div>
    <div class="back__rule-bottom"></div>
  </section>

</main>
</body>
</html>
```